Hydrographic business needs a business card that reaches hunters and off-road enthusiasts

We need a business card for a new hydrographics company catering to customers such as hunters, off-road ATV riders and custom vehicle enthusiasts. A western theme is preferred but professional. Our service should be thought of as upper end graphic design on firearms, off road vehicles, motorcycles, etc... See www.caldorfx.com for ideas on patterns, colors, etc...

Target Market(s)

Hunters, off road enthusiasts, custom car enthusiasts, motorcycle riders...

Industry/Entity Type

Graphic Design

```html
<!DOCTYPE html>
<html lang="en">
<head>
<meta charset="utf-8">
<title>Caldor Hydro-Graphics — Business Card</title>
<link rel="stylesheet" href="https://fonts.googleapis.com/css2?family=Arimo:wght@400;700&display=swap">
<style>
  :root {
    --page-bg: #e7e2dc;
    --brand-red: #a6283a;
    --card-white: #ffffff;
    --ink: #1d1d1d;
    --camo-light: #c9c3b6;
    --camo-mid: #9a9583;
    --camo-moss: #6f7557;
    --camo-bark: #5d5645;
    --name-tint: rgba(176, 110, 96, 0.55);
    --card-shadow: 0 6px 18px rgba(0, 0, 0, 0.18);
  }
  * { box-sizing: border-box; margin: 0; padding: 0; }
  html, body {
    width: 1200px;
    height: 914px;
    overflow: hidden;
    background: var(--page-bg);
    font-family: "Arimo", Arial, sans-serif;
  }
  .canvas {
    position: relative;
    width: 1200px;
    height: 914px;
  }
  .card {
    position: absolute;
    left: 250px;
    width: 700px;
    height: 400px;
    overflow: hidden;
    background: var(--card-white);
    box-shadow: var(--card-shadow);
  }
  .card--front { top: 37px; }
  .card--back  { top: 477px; }

  .card__art {
    position: absolute;
    inset: 0;
    width: 100%;
    height: 100%;
  }

  /* Front */
  .front-brand {
    position: absolute;
    left: 70px;
    top: 262px;
    font-size: 52px;
    font-weight: 700;
    color: var(--brand-red);
    letter-spacing: 0.5px;
  }

  /* Back */
  .holder {
    position: absolute;
    left: 28px;
    bottom: 54px;
    color: var(--card-white);
    display: flex;
    align-items: flex-end;
    gap: 8px;
  }
  .holder__title { font-size: 14px; padding-bottom: 2px; }
  .holder__name  { font-size: 34px; }

  .back-brand {
    position: absolute;
    left: 392px;
    top: 38px;
    font-size: 27px;
    font-weight: 700;
    color: var(--brand-red);
  }
  .contact-list {
    position: absolute;
    left: 400px;
    top: 104px;
    list-style: none;
  }
  .contact-list__item {
    display: flex;
    align-items: flex-start;
    gap: 18px;
    height: 46px;
    font-size: 19px;
    color: var(--ink);
    line-height: 24px;
  }
  .contact-list__icon {
    flex: none;
    width: 26px;
    height: 26px;
  }
</style>
</head>
<body>
<main class="canvas">

  <!-- Front of card -->
  <section class="card card--front">
    <svg class="card__art" viewBox="0 0 700 400" role="img" aria-label="Woodland camouflage pattern of shed antlers, mossy bark, mushrooms and autumn leaves">
      <defs>
        <linearGradient id="camoFront" x1="0" y1="0" x2="1" y2="1">
          <stop offset="0" stop-color="#a8a291"/>
          <stop offset="0.35" stop-color="#c9c3b6"/>
          <stop offset="0.6" stop-color="#8e8a74"/>
          <stop offset="0.85" stop-color="#7a7a5e"/>
          <stop offset="1" stop-color="#a58a5a"/>
        </linearGradient>
      </defs>
      <rect width="700" height="400" fill="url(#camoFront)"/>
    </svg>
    <div class="front-brand">Caldor Hydro-Graphics</div>
  </section>

  <!-- Back of card -->
  <section class="card card--back">
    <svg class="card__art" viewBox="0 0 700 400" aria-hidden="true">
      <defs>
        <linearGradient id="camoBack" x1="0" y1="0" x2="1" y2="1">
          <stop offset="0" stop-color="#b3ad9d"/>
          <stop offset="0.4" stop-color="#8f8c74"/>
          <stop offset="0.75" stop-color="#a39d8c"/>
          <stop offset="1" stop-color="#7d7860"/>
        </linearGradient>
      </defs>
      <g role="img" aria-label="Woodland camouflage pattern of shed antlers, mossy bark and mushrooms">
        <rect width="700" height="400" fill="url(#camoBack)"/>
      </g>
      <rect class="holder-band" x="0" y="300" width="380" height="100" fill="var(--name-tint)"/>
      <circle cx="512" cy="208" r="272" fill="var(--brand-red)"/>
      <circle cx="522" cy="216" r="254" fill="var(--card-white)"/>
    </svg>

    <div class="holder">
      <span class="holder__title">Title</span>
      <span class="holder__name">Your Name</span>
    </div>

    <div class="back-brand">Caldor Hydro-Graphics</div>

    <ul class="contact-list">
      <li class="contact-list__item">
        <svg class="contact-list__icon" viewBox="0 0 26 26" aria-hidden="true">
          <rect width="26" height="26" rx="5" fill="var(--brand-red)"/>
          <path d="M8 7c1-1 2-1 2.5 0l1.5 2.5c.4.7 0 1.3-.6 1.8l-.8.6c.8 1.7 2 2.9 3.7 3.7l.6-.8c.5-.6 1.1-1 1.8-.6L19 16.5c1 .5 1 1.5 0 2.5-1.5 1.5-4 .8-6.5-1.7S6.5 8.5 8 7z" fill="#fff"/>
        </svg>
        <span>(555) 214-7780</span>
      </li>
      <li class="contact-list__item">
        <svg class="contact-list__icon" viewBox="0 0 26 26" aria-hidden="true">
          <rect width="26" height="26" rx="5" fill="var(--brand-red)"/>
          <rect x="6" y="8" width="14" height="10" fill="none" stroke="#fff" stroke-width="1.6"/>
          <path d="M6 8l7 6 7-6M6 18l5-5M20 18l-5-5" fill="none" stroke="#fff" stroke-width="1.4"/>
        </svg>
        <span>caldorfx@mailbox.com</span>
      </li>
      <li class="contact-list__item">
        <svg class="contact-list__icon" viewBox="0 0 26 26" aria-hidden="true">
          <rect width="26" height="26" rx="5" fill="var(--brand-red)"/>
          <circle cx="13" cy="13" r="7" fill="none" stroke="#fff" stroke-width="1.6"/>
          <path d="M6 13h14M13 6c-3 3.5-3 10.5 0 14M13 6c3 3.5 3 10.5 0 14" fill="none" stroke="#fff" stroke-width="1.2"/>
        </svg>
        <span>www.caldorfx.com</span>
      </li>
      <li class="contact-list__item">
        <svg class="contact-list__icon" viewBox="0 0 26 26" aria-hidden="true">
          <rect width="26" height="26" rx="5" fill="var(--brand-red)"/>
          <path d="M5.5 13.5L13 6.5l7.5 7" fill="none" stroke="#fff" stroke-width="1.8"/>
          <path d="M8 13v7h4v-4h2v4h4v-7l-5-4.5z" fill="#fff"/>
        </svg>
        <span>1840 Pinecrest Trail,<br>Dry Creek, TX, United States</span>
      </li>
    </ul>
  </section>

</main>
</body>
</html>
```